Record Label Needs Design for CD Case, Booklet, and CD...

We are a christian record label looking to make a difference in this world.

We need 3 files -
The front and back of CD case and the actual CD graphics.

It is entitled

"Halvane Sound and Friends Summer Sampler 2014"

We will give you the artists and songs on the CD.

Please send IDEAS WE ARE OPEN TO ANYTHING!!!

you can find information on our record label at www.halvanesound.com or www.facebook.com/halvanesound

The 2 artists on the summer sampler are Marrowfen - and Copper Harbour

I have pictures of Marrowfen attached below, and pictures of copper harbour below...

marrowfenmusic.com has their logo
copper harbours logo is attached...

This is a guaranteed payout and Ive had much luck with pixel guild. Looking forward to another successful contest.

dale@halvanesound.com

Reason: We haven't had any responses yet so we extended this out a few days!

Reason: We need better designs...

Come on guys!  Send in some new designs!  I am not hard to please!  I just updated the color schemes, etc....

Target Market(s)

Christians

Industry/Entity Type

Artists

Colors
d3a5cc
ed9dc4
8768ae

Requirements
Must have
• Positivity
Nice to have
• Doves are nice
Should not have
• Crosses

```html
<!DOCTYPE html>
<html lang="en">
<head>
<meta charset="utf-8">
<title>Halvane Sound and Friends – Summer Sampler 2014</title>
<link rel="stylesheet" href="https://fonts.googleapis.com/css2?family=Almendra&display=swap">
<style>
  :root {
    --plum-deep: #7a2580;
    --plum-mid: #a45aa8;
    --mist: #ece6f0;
    --violet-deep: #4a30a8;
    --violet-mid: #8768ae;
    --lavender-light: #d8d2f0;
    --band-pink: #e35ee0;
    --band-lavender: #cfcaf0;
    --edge-line: #2a1a30;
    --ink: #120a14;
  }
  html, body {
    margin: 0;
    padding: 0;
    width: 1200px;
    height: 920px;
    overflow: hidden;
    background: #ffffff;
  }
  .cover {
    display: block;
    width: 1200px;
    height: 920px;
  }
  .cover-title {
    font-family: "Almendra", "Papyrus", serif;
    fill: var(--ink);
  }
  .title-main { font-size: 80px; }
  .title-sub { font-size: 80px; }
</style>
</head>
<body>
<svg class="cover" viewBox="0 0 1200 920" xmlns="http://www.w3.org/2000/svg">
  <defs>
    <linearGradient id="groundTone" x1="0" y1="0" x2="0.25" y2="1">
      <stop offset="0" stop-color="var(--plum-deep)"/>
      <stop offset="0.3" stop-color="var(--plum-mid)"/>
      <stop offset="0.5" stop-color="var(--mist)"/>
      <stop offset="0.72" stop-color="var(--violet-mid)"/>
      <stop offset="1" stop-color="var(--violet-deep)"/>
    </linearGradient>
    <radialGradient id="centreGlow" cx="0.65" cy="0.45" r="0.45">
      <stop offset="0" stop-color="#ffffff" stop-opacity="0.8"/>
      <stop offset="1" stop-color="#ffffff" stop-opacity="0"/>
    </radialGradient>
    <radialGradient id="emblemGlow" cx="0.5" cy="0.5" r="0.5">
      <stop offset="0" stop-color="var(--lavender-light)" stop-opacity="0.95"/>
      <stop offset="0.55" stop-color="var(--lavender-light)" stop-opacity="0.55"/>
      <stop offset="1" stop-color="var(--lavender-light)" stop-opacity="0"/>
    </radialGradient>
    <radialGradient id="upperGlow" cx="0.5" cy="0.5" r="0.5">
      <stop offset="0" stop-color="#f4dcf2" stop-opacity="0.45"/>
      <stop offset="1" stop-color="#f4dcf2" stop-opacity="0"/>
    </radialGradient>
    <radialGradient id="vignette" cx="0.5" cy="0.5" r="0.75">
      <stop offset="0.6" stop-color="#000000" stop-opacity="0"/>
      <stop offset="1" stop-color="#1a0a24" stop-opacity="0.55"/>
    </radialGradient>
    <filter id="chalkGrain" x="0" y="0" width="100%" height="100%">
      <feTurbulence type="fractalNoise" baseFrequency="0.9" numOctaves="2" seed="4" result="noise"/>
      <feColorMatrix in="noise" type="matrix"
        values="0 0 0 0 1  0 0 0 0 1  0 0 0 0 1  0 0 0 1.6 -0.7" result="specks"/>
      <feComposite in="specks" in2="SourceGraphic" operator="in"/>
    </filter>
  </defs>

  <g class="cover-ground" role="img" aria-label="Grainy chalk texture in plum and violet">
    <rect width="1200" height="920" fill="url(#groundTone)"/>
    <rect width="1200" height="920" fill="url(#centreGlow)"/>
    <rect width="1200" height="920" fill="#ffffff" filter="url(#chalkGrain)" opacity="0.35"/>
  </g>

  <ellipse class="emblem-upper" role="img" aria-label="Faint chalk heart outline decoration"
    cx="530" cy="220" rx="220" ry="150" fill="url(#upperGlow)"/>

  <ellipse class="emblem-lower" role="img" aria-label="Large faint lavender heart-and-figure emblem in chalk"
    cx="600" cy="720" rx="340" ry="260" fill="url(#emblemGlow)"/>

  <polygon class="band band-pink" points="0,432 1200,22 1200,112 0,528" fill="var(--band-pink)" opacity="0.85"/>
  <polygon class="band band-lavender" points="0,528 1200,112 1200,205 0,615" fill="var(--band-lavender)" opacity="0.7"/>

  <rect class="vignette" width="1200" height="920" fill="url(#vignette)"/>

  <line class="edge-line" x1="80" y1="0" x2="80" y2="920" stroke="var(--edge-line)" stroke-width="2" opacity="0.7"/>
  <line class="edge-line" x1="1120" y1="0" x2="1120" y2="920" stroke="var(--edge-line)" stroke-width="2" opacity="0.7"/>

  <text class="cover-title title-main" transform="translate(140 388) rotate(-15.5)"
    textLength="965" lengthAdjust="spacing">Halvane Sound and Friends</text>
  <text class="cover-title title-sub" transform="translate(320 522) rotate(-21.5)"
    textLength="830" lengthAdjust="spacing">Summer Sampler 2014</text>
</svg>
</body>
</html>
```